Geschäftspapiere
Zielgruppe
Die BRIO Salbe gibt ein zuverlässige Gefühl, durch ein innovatives Naturprodukt erstaunlich schnelle, wirkungsvolle Hilfe bei Schmerzen des Bewegungsapparates und bei Hautschäden zu erhalten und dabei gleichzeitig die Haut zu pflegen.
Wir wollen jetzt stärker auf die Zielgruppe TCM Praxis, Chiropraktiker, Physiotherapie gehen und wollen nun eine Preisliste dafür erstellen.
Aufgabenstellung
Zielgruppe ist B2B, TCM Praxis, Chiropraktiker, Physiotherapie.
Die Preisliste sollte auf den Briefpapier erstellt werden. Bitte an Farben, Logos etc. von der Webseite nehmen.

```html
<!DOCTYPE html>
<html lang="de">
<head>
<meta charset="utf-8">
<title>Preisliste – BRIO Naturbalsame</title>
<link href="https://fonts.googleapis.com/css2?family=Roboto:wght@400;500;700;900&family=Source+Sans+3:wght@400;600&display=swap" rel="stylesheet">
<style>
  :root{
    --bg:#d9d9d9;
    --paper:#fbfbfb;
    --ink:#1b1b1b;
    --muted:#555;
    --orange:#f0a210;
    --orange-deep:#e8860c;
    --amber:#f7b52a;
    --red:#d81f0c;
    --red-deep:#b80e06;
    --white:#ffffff;
  }
  *{box-sizing:border-box;margin:0;padding:0}
  html,body{width:1200px;height:1200px;overflow:hidden;background:var(--bg)}
  body{font-family:"Roboto",Arial,sans-serif;color:var(--ink);position:relative}

  .page{position:absolute;left:190px;top:25px;width:820px;height:1150px;background:var(--paper);
        box-shadow:0 6px 24px rgba(0,0,0,.18);overflow:hidden}
  .page__edge{position:absolute;right:0;top:0;width:12px;height:100%;background:var(--orange)}
  .fold-mark{position:absolute;left:0;top:400px;width:22px;height:2px;background:var(--orange)}

  .sender{position:absolute;left:90px;top:205px;font-family:"Source Sans 3",sans-serif;font-size:10px;color:var(--muted)}
  .sender strong{font-weight:600;color:#333}
  .sender .dot{color:var(--orange)}

  .brand-halo{position:absolute;right:50px;top:40px;width:280px;height:200px;
              border-bottom:3px solid #d8d8d8;border-radius:0 0 140px 140px;}
  .brand{position:absolute;right:82px;top:95px;width:220px;text-align:center}
  .brand__row{display:flex;align-items:center;justify-content:center;gap:12px}
  .brand__dot{width:34px;height:34px;border-radius:50%;background:var(--orange)}
  .brand__name{font-family:"Roboto",sans-serif;font-weight:900;font-size:46px;letter-spacing:1px;color:var(--ink);line-height:1}
  .brand__sub{margin-top:8px;font-size:13px;letter-spacing:4px;color:#333}
  .brand__tag{margin-top:8px;font-size:13px;font-weight:700;letter-spacing:2.5px;color:var(--orange-deep)}

  .title{position:absolute;left:0;right:12px;top:400px;text-align:center;font-size:34px;font-weight:500}
  .intro{position:absolute;left:90px;right:100px;top:455px;text-align:center;font-size:15px;line-height:1.5}

  .cards{position:absolute;left:0;top:0;width:100%;height:100%}
  .card{position:absolute;border-radius:26px;overflow:hidden;color:var(--white);
        box-shadow:0 8px 18px rgba(0,0,0,.22);
        background:radial-gradient(circle at 10% 45%,var(--red) 0,rgba(216,31,12,0) 35%),
                   linear-gradient(160deg,var(--orange-deep) 0%,var(--amber) 55%,var(--orange) 100%)}
  .card--starter{left:95px;top:550px;width:185px;height:330px}
  .card--special{left:315px;top:562px;width:215px;height:380px}
  .card--premium{left:565px;top:605px;width:185px;height:335px}

  .card__icon{position:absolute;left:50%;top:28px;width:76px;height:76px;margin-left:-38px;border-radius:50%;
              border:2px solid var(--white);
              background:radial-gradient(circle at 50% 55%,#fde59a 0,#f39a2a 45%,#d9430f 100%)}
  .card--special .card__icon{width:86px;height:86px;margin-left:-43px}

  .card__dome{position:absolute;left:-18px;right:-18px;height:300px;border-radius:50%;border:3px solid var(--white);
              background:linear-gradient(180deg,var(--amber),var(--orange))}
  .card--starter .card__dome,.card--premium .card__dome{top:112px}
  .card--special .card__dome{top:135px;background:radial-gradient(circle at 50% 30%,var(--red) 0,#e4480c 40%,var(--orange) 75%)}
  .card--premium .card__dome{background:radial-gradient(circle at 50% 30%,#e4600e 0,var(--orange-deep) 45%,var(--orange) 80%)}

  .card__arc{position:absolute;left:50%;width:110px;height:110px;margin-left:-55px;border-radius:50%;
             border:2px solid transparent;border-bottom-color:var(--white)}
  .card--starter .card__arc,.card--premium .card__arc{top:118px}
  .card--special .card__arc{top:148px;width:130px;height:130px;margin-left:-65px}

  .card__price{position:absolute;left:0;right:0;text-align:center;font-size:27px;font-weight:500;line-height:1.2}
  .card--starter .card__price,.card--premium .card__price{top:160px}
  .card--special .card__price{top:192px;font-size:32px}

  .card__qty{position:absolute;left:0;right:0;text-align:center;font-size:19px;line-height:1.2}
  .card--starter .card__qty,.card--premium .card__qty{top:242px}
  .card--special .card__qty{top:292px;font-size:21px}

  .card__band{position:absolute;left:0;right:0;bottom:0;height:52px;border-top:2px solid var(--white);
              display:flex;align-items:center;justify-content:center;
              font-size:19px;font-weight:900;letter-spacing:.5px}
  .card--starter .card__band{background:linear-gradient(90deg,#f0b430,#f5c04a)}
  .card--special .card__band{background:linear-gradient(90deg,var(--red-deep),var(--red))}
  .card--premium .card__band{background:linear-gradient(90deg,var(--orange-deep),#e46a10)}

  .body-text{position:absolute;left:90px;right:90px;top:962px;font-size:14px;line-height:1.5}

  .footer{position:absolute;left:0;bottom:0;width:100%;height:86px;background:var(--orange);
          display:flex;gap:28px;padding:12px 40px 0 90px;color:var(--white);
          font-family:"Source Sans 3",sans-serif;font-size:10.5px;line-height:1.5}
  .footer__col{padding-right:24px;border-right:2px solid var(--white)}
  .footer__col:last-child{border-right:none}
  .footer__col strong{font-weight:600}
  .footer dl{display:grid;grid-template-columns:auto auto;column-gap:12px}
  .footer dt{font-weight:600}
</style>
</head>
<body>
  <main class="page">
    <div class="page__edge"></div>
    <div class="fold-mark"></div>

    <p class="sender"><strong>Kellmann Vital Vertrieb GmbH</strong> <span class="dot">-</span> Lindenhofstr. 14 <span class="dot">-</span> 80335 München</p>

    <div class="brand-halo"></div>
    <div class="brand">
      <div class="brand__row"><span class="brand__dot"></span><span class="brand__name">BRIO</span></div>
      <p class="brand__sub">NATURBALSAME</p>
      <p class="brand__tag">ALWAYS BRIO</p>
    </div>

    <h1 class="title">Preisliste</h1>
    <p class="intro">Lorem ipsum dolor sit amet, consectetuer adipiscing elit, sed diam nonummy nibh euismod tincidunt ut laoreet dolore magna aliquam erat volutpat. Ut wisi enim ad</p>

    <section class="cards">
      <article class="card card--starter">
        <div class="card__icon" role="img" aria-label="Lotusblüten-Symbol"></div>
        <div class="card__dome"></div>
        <div class="card__arc"></div>
        <p class="card__price">70,-</p>
        <p class="card__qty">5 Tuben</p>
        <p class="card__band">STARTER</p>
      </article>
      <article class="card card--special">
        <div class="card__icon" role="img" aria-label="Lotusblüten-Symbol"></div>
        <div class="card__dome"></div>
        <div class="card__arc"></div>
        <p class="card__price">500,-</p>
        <p class="card__qty">50 Tuben</p>
        <p class="card__band">SPECIAL</p>
      </article>
      <article class="card card--premium">
        <div class="card__icon" role="img" aria-label="Lotusblüten-Symbol"></div>
        <div class="card__dome"></div>
        <div class="card__arc"></div>
        <p class="card__price">300,-</p>
        <p class="card__qty">20 Tuben</p>
        <p class="card__band">PREMIUM</p>
      </article>
    </section>

    <p class="body-text">Lorem ipsum dolor sit amet, consectetuer adipiscing elit, sed diam nonummy nibh euismod tincidunt ut laoreet dolore magna aliquam erat volutpat. Ut wisi enim ad Lorem ipsum dolor sit amet, consectetuer adipiscing elit, sed diam nonummy nibh euismod tincidunt ut laoreet dolore magna aliquam erat volutpat. Ut wisi enim ad minim.</p>

    <footer class="footer">
      <div class="footer__col">
        <strong>Kellmann Vital Vertrieb GmbH</strong><br>
        Lindenhofstr. 14<br>
        80335 München<br>
        Deutschland
      </div>
      <div class="footer__col">
        <dl>
          <dt>Telefon:</dt><dd>0049 89 123 456 70</dd>
          <dt>Telefax:</dt><dd>0049 89 123 456 71</dd>
          <dt>E-Mail:</dt><dd>bestellung@kellmann-vital.de</dd>
        </dl>
      </div>
      <div class="footer__col">
        <strong>Gesellschafter:</strong> Jonas Weber
      </div>
    </footer>
  </main>
</body>
</html>
```